Birthday Party Invitation

I need to create a "save the date" for my birthday party.
Text:

Save the Date
Saturday, 6 December 2014
9 pm
Club la Brisa, Lindenweg 42, 8005 Zürich
BLACK IT OUT
SAVE IT!
RESERVE THE TIME
WRITE IT DOWN
HOLD THE DATE to LET YOUR HAIR DOWN and Party with Me.

Target Market(s)

Friends

Industry/Entity Type

Club

Requirements
Must have
• I want the flyer to look classy and sexy at the same time.
Nice to have
• Picture on the left or right, then text white on black background. Maybe a simple frame. Not too playful, rather simple, elegant and no graphics. Just picture and text.

```html
<!DOCTYPE html>
<html lang="en">
<head>
<meta charset="utf-8">
<title>Save the Date – Birthday Party</title>
<link rel="stylesheet" href="https://fonts.googleapis.com/css2?family=PT+Sans:wght@400;700&family=Pinyon+Script&display=swap">
<style>
  :root {
    --backdrop: #d9dcd6;
    --card-black: #0b0b0b;
    --ink-white: #f4f4f4;
    --divider: #d0d0d0;
    --photo-dark: #1a120d;
    --photo-warm: #5a3a22;
    --photo-red: #8a1f1c;
    --ornament-tone: #3a3a3a;
  }
  * { margin: 0; padding: 0; box-sizing: border-box; }
  html, body {
    width: 1200px;
    height: 800px;
    overflow: hidden;
    background: var(--backdrop);
  }
  .invitation-card {
    position: absolute;
    left: 40px;
    top: 50px;
    width: 1120px;
    height: 700px;
    display: flex;
    background: var(--card-black);
    box-shadow: 0 6px 18px rgba(0,0,0,0.25);
  }
  .portrait-area {
    width: 555px;
    height: 100%;
    background:
      radial-gradient(ellipse 40% 30% at 48% 72%, var(--photo-red) 0%, rgba(138,31,28,0) 100%),
      radial-gradient(ellipse 55% 60% at 45% 40%, var(--photo-warm) 0%, var(--photo-dark) 75%);
  }
  .panel-divider {
    width: 4px;
    height: 100%;
    background: var(--divider);
    margin: 0 3px;
  }
  .details-panel {
    flex: 1;
    position: relative;
    display: flex;
    flex-direction: column;
    align-items: center;
    color: var(--ink-white);
    font-family: "PT Sans", sans-serif;
    font-weight: 700;
    text-align: center;
  }
  .title-frame {
    margin-top: 36px;
    width: 230px;
    height: 96px;
    display: flex;
    align-items: center;
    justify-content: center;
  }
  .title-frame svg { position: absolute; }
  .save-the-date {
    position: relative;
    font-family: "Pinyon Script", cursive;
    font-weight: 400;
    font-size: 30px;
    color: var(--ink-white);
  }
  .event-info {
    margin-top: 70px;
    font-size: 21px;
    line-height: 30px;
  }
  .call-to-action {
    margin-top: 30px;
    font-size: 21px;
    line-height: 30px;
  }
  .call-to-action + .call-to-action { margin-top: 30px; }
  .connector { font-weight: 400; }
  .footer-flourish {
    position: absolute;
    left: 40px;
    right: 40px;
    bottom: 18px;
    height: 56px;
    background: linear-gradient(to top, var(--ornament-tone), rgba(58,58,58,0));
  }
</style>
</head>
<body>
  <main class="invitation-card">
    <div class="portrait-area" role="img" aria-label="Portrait photo of the host in a red festive dress with white fur trim and a fur hat"></div>
    <div class="panel-divider"></div>
    <section class="details-panel">
      <div class="title-frame">
        <svg width="230" height="96" viewBox="0 0 230 96" aria-hidden="true">
          <rect x="4" y="4" width="222" height="88" rx="8" fill="none" stroke="#f4f4f4" stroke-width="2"/>
          <rect x="12" y="12" width="206" height="72" rx="5" fill="none" stroke="#f4f4f4" stroke-width="1"/>
        </svg>
        <h1 class="save-the-date">Save the Date</h1>
      </div>
      <p class="event-info">
        Saturday, 6 December 2014<br>
        9 pm<br>
        Club la Brisa, Lindenweg 42, 8005 Zürich
      </p>
      <p class="call-to-action">
        BLACK IT OUT<br>
        SAVE IT!<br>
        RESERVE THE TIME
      </p>
      <p class="call-to-action">
        WRITE IT DOWN<br>
        HOLD THE DATE<br>
        <span class="connector">to</span><br>
        LET YOUR HAIR DOWN<br>
        <span class="connector">and</span><br>
        Party with Me.
      </p>
      <div class="footer-flourish" role="img" aria-label="Decorative white scroll ornament along the bottom edge"></div>
    </section>
  </main>
</body>
</html>
```